1/2 Page add for BRMTL Conference

We are looking for a 1/2 page ad to support the annual BRMTL conference. I want to encourage the attendees to come to our both so we can explain how they can save money on food and supplies. here is a link to the conference. https://www.brmtl-example.org/conference/ here is our website www.pantrywisehub-example.com - the what we do can be captured in the ad. We will be at booth 505. Our goal is to get people to our booth #505 to explain the services that we provide –

Discounted food pricing
Free menu planning/design
Use of Registered Dietitian
Huge selection of discounted PPE and other necessary supplies to run any child care center

We have over 6000 members in 46 States and work with both small and large food distributors. We have been a sponsor of the association for the last 10 years.

Target Market(s)

Child care centers

Requirements
Must have
• Booth number -outline of what we do --- Stress we are a FREE service getting our members reduced pricing on food and supplies

```html
<!DOCTYPE html>
<html lang="en">
<head>
<meta charset="utf-8">
<title>PantryWise Hub – Booth #505 Half Page Ad</title>
<link rel="stylesheet" href="https://fonts.googleapis.com/css2?family=Montserrat:ital,wght@0,500;0,600;0,700;0,800;1,500&display=swap">
<style>
  :root {
    --navy: #163f7a;
    --blue: #1f6fb8;
    --sky: #3d9ad9;
    --green: #7cbf3a;
    --green-dark: #5fa22a;
    --white: #ffffff;
    --page: #eef0f3;
    --photo-warm: #e9c7a4;
    --photo-cool: #b9d3e6;
  }
  * { box-sizing: border-box; margin: 0; padding: 0; }
  html, body { width: 863px; height: 1200px; overflow: hidden; }
  body {
    background: var(--page);
    font-family: "Montserrat", Arial, sans-serif;
    position: relative;
  }
  .ad {
    position: absolute;
    left: 20px; top: 318px;
    width: 823px; height: 564px;
    background: var(--white);
    overflow: hidden;
    box-shadow: 0 2px 10px rgba(0,0,0,.12);
  }
  .ad__photo {
    position: absolute;
    left: 0; top: 0;
    width: 520px; height: 450px;
    background: linear-gradient(135deg, var(--photo-cool) 0%, #efe4d6 40%, var(--photo-warm) 75%, #c98d5d 100%);
  }
  .ad__curves { position: absolute; left: 0; top: 0; width: 823px; height: 564px; }
  .booth-tab {
    position: absolute;
    right: 0; top: 22px;
    width: 350px; height: 40px;
    background: var(--green);
    color: var(--white);
    font-weight: 800;
    font-size: 24px;
    text-align: right;
    padding: 6px 26px 0 0;
    border-radius: 22px 0 0 22px;
  }
  .event-name {
    position: absolute;
    right: 26px; top: 78px;
    font-weight: 700;
    font-size: 15.5px;
    color: var(--navy);
    text-align: right;
  }
  .headline {
    position: absolute;
    right: 26px; top: 100px;
    width: 380px;
    font-weight: 800;
    font-size: 31px;
    line-height: 1.08;
    color: var(--navy);
    text-align: right;
    text-transform: uppercase;
  }
  .services {
    position: absolute;
    right: 22px; top: 186px;
    list-style: none;
  }
  .services__item {
    display: flex;
    justify-content: flex-end;
    align-items: center;
    gap: 10px;
    height: 34px;
    font-size: 15px;
    font-weight: 600;
    color: var(--blue);
  }
  .services__icon {
    width: 27px; height: 27px;
    border-radius: 50%;
    background: var(--blue);
    display: flex; align-items: center; justify-content: center;
    flex: none;
  }
  .free-note {
    position: absolute;
    right: 26px; top: 364px;
    width: 330px;
    text-align: right;
    font-style: italic;
    font-weight: 500;
    font-size: 13px;
    line-height: 1.3;
    color: var(--navy);
  }
  .visit-badge {
    position: absolute;
    left: 330px; top: 296px;
    width: 104px; height: 104px;
    border-radius: 50%;
    background: var(--green);
    border: 4px solid var(--white);
    color: var(--white);
    text-align: center;
    font-weight: 800;
    font-size: 12.5px;
    line-height: 1.2;
    padding-top: 24px;
  }
  .brand {
    position: absolute;
    left: 30px; top: 480px;
    display: flex; align-items: center; gap: 12px;
  }
  .brand__mark { width: 34px; height: 34px; background: var(--green); border-radius: 50%; }
  .brand__name { font-weight: 700; font-size: 27px; color: var(--navy); }
  .brand__tag {
    position: absolute;
    left: 76px; top: 520px;
    font-size: 10px; font-weight: 500; color: var(--navy);
  }
  .event-info {
    position: absolute;
    right: 26px; top: 470px;
    text-align: right;
    color: var(--white);
  }
  .event-info__date { font-weight: 700; font-size: 19px; }
  .event-info__place { font-weight: 500; font-size: 16px; margin-top: 2px; }
  .event-info__web { font-weight: 700; font-size: 17px; margin-top: 8px; }
</style>
</head>
<body>
  <section class="ad">
    <div class="ad__photo" role="img" aria-label="Photo of a mother and two young children in chef hats preparing vegetables in a kitchen"></div>

    <svg class="ad__curves" viewBox="0 0 823 564" aria-hidden="true">
      <path d="M430 0 C 560 120, 520 320, 420 452 L 823 452 L 823 0 Z" fill="var(--white)"/>
      <path d="M430 0 C 560 120, 520 320, 420 452" fill="none" stroke="var(--green)" stroke-width="7"/>
      <path d="M0 430 C 200 470, 380 440, 823 400 L 823 564 L 0 564 Z" fill="var(--green)"/>
      <path d="M0 442 C 200 482, 380 452, 823 414 L 823 564 L 0 564 Z" fill="var(--white)"/>
      <path d="M440 564 C 470 500, 540 450, 823 430 L 823 564 Z" fill="var(--blue)"/>
    </svg>

    <div class="booth-tab">BOOTH #505</div>
    <p class="event-name">2022 National Youth Meals Conference</p>
    <h1 class="headline">Save money on food and supplies</h1>

    <ul class="services">
      <li class="services__item">Discounted food pricing
        <span class="services__icon"><svg width="15" height="15" viewBox="0 0 16 16"><path d="M3 8.5l3 3 7-7" fill="none" stroke="#fff" stroke-width="2.4" stroke-linecap="round" stroke-linejoin="round"/></svg></span></li>
      <li class="services__item">Free menu planning/design
        <span class="services__icon"><svg width="15" height="15" viewBox="0 0 16 16"><path d="M3 8.5l3 3 7-7" fill="none" stroke="#fff" stroke-width="2.4" stroke-linecap="round" stroke-linejoin="round"/></svg></span></li>
      <li class="services__item">Use of Registered Dietitian
        <span class="services__icon"><svg width="15" height="15" viewBox="0 0 16 16"><path d="M3 8.5l3 3 7-7" fill="none" stroke="#fff" stroke-width="2.4" stroke-linecap="round" stroke-linejoin="round"/></svg></span></li>
      <li class="services__item">Huge selection of discounted PPE
        <span class="services__icon"><svg width="15" height="15" viewBox="0 0 16 16"><path d="M3 8.5l3 3 7-7" fill="none" stroke="#fff" stroke-width="2.4" stroke-linecap="round" stroke-linejoin="round"/></svg></span></li>
      <li class="services__item">Supplies to run any child care center
        <span class="services__icon"><svg width="15" height="15" viewBox="0 0 16 16"><path d="M3 8.5l3 3 7-7" fill="none" stroke="#fff" stroke-width="2.4" stroke-linecap="round" stroke-linejoin="round"/></svg></span></li>
    </ul>

    <p class="free-note">We are a FREE service getting our members reduced pricing on food and supplies</p>

    <div class="visit-badge">VISIT US AT<br>BOOTH #505<br>APRIL 18-22</div>

    <div class="brand">
      <span class="brand__mark"></span>
      <span class="brand__name">PantryWise Hub</span>
    </div>
    <p class="brand__tag">Member savings network</p>

    <div class="event-info">
      <p class="event-info__date">APRIL 18-22, 2022</p>
      <p class="event-info__place">New Orleans, Louisiana</p>
      <p class="event-info__web">www.pantrywisehub-example.com</p>
    </div>
  </section>
</body>
</html>
```